Amber Lantern Cafe Business Card

We need a business card design for a new European Cafe. Main menu will be coffee and deserts.

Requirements
Must have
• Logo - 1 of the attached versions
Address - TBA (you can use 487 Morrow Ave Unit 9 for now)
Phone - TBA (you can use 555-238-4176 for now)

```html
<!DOCTYPE html>
<html lang="en">
<head>
<meta charset="utf-8">
<title>Amber Lantern Cafe – Business Card</title>
<link href="https://fonts.googleapis.com/css2?family=Open+Sans:wght@400;600;700&display=swap" rel="stylesheet">
<style>
  :root {
    --cafe-red: #9c1a20;
    --cafe-red-dark: #7a1116;
    --cafe-red-light: #b0242a;
    --card-white: #ffffff;
    --card-mist: #ececec;
    --stage: #e4e4e4;
    --soft-text: #f3d6d7;
  }
  * { box-sizing: border-box; margin: 0; padding: 0; }
  html, body { width: 1200px; height: 900px; overflow: hidden; }
  body {
    background: var(--stage);
    font-family: "Open Sans", Arial, sans-serif;
    display: flex;
    flex-direction: column;
    align-items: center;
    justify-content: center;
    gap: 56px;
  }
  .card {
    position: relative;
    width: 620px;
    height: 354px;
    border-radius: 24px;
    overflow: hidden;
    box-shadow: 0 6px 18px rgba(0,0,0,0.18);
  }
  .card-art { position: absolute; inset: 0; }

  /* Front side */
  .brand {
    position: absolute;
    left: 40px;
    top: 40px;
    display: flex;
    align-items: center;
    gap: 18px;
  }
  .brand-square {
    width: 82px;
    height: 82px;
    background: var(--cafe-red);
    border-radius: 4px;
  }
  .brand-name {
    display: flex;
    flex-direction: column;
    align-items: center;
    color: var(--cafe-red);
    font-weight: 600;
    line-height: 1;
  }
  .brand-name .wordmark { font-size: 36px; letter-spacing: -0.5px; }
  .brand-name .sub {
    display: flex;
    align-items: center;
    gap: 10px;
    font-size: 22px;
    margin-top: 4px;
    width: 100%;
  }
  .brand-name .sub::before,
  .brand-name .sub::after {
    content: "";
    flex: 1;
    height: 2px;
    background: currentColor;
  }

  .contact {
    position: absolute;
    left: 40px;
    top: 212px;
    color: var(--card-white);
  }
  .contact .person { font-size: 18px; font-weight: 700; }
  .contact .role { font-size: 13px; color: var(--soft-text); margin-bottom: 14px; }
  .contact dl {
    display: grid;
    grid-template-columns: 62px auto;
    font-size: 14px;
    line-height: 1.45;
  }
  .contact dt { color: var(--soft-text); }

  .location {
    position: absolute;
    right: 36px;
    top: 212px;
    color: var(--soft-text);
    font-size: 13px;
    line-height: 1.5;
  }

  /* Back side */
  .card--back {
    background: radial-gradient(circle at 45% 40%, var(--cafe-red-light), var(--cafe-red) 55%, var(--cafe-red-dark));
  }
  .back-brand {
    position: absolute;
    inset: 0;
    display: flex;
    flex-direction: column;
    align-items: center;
    justify-content: center;
    gap: 18px;
  }
  .back-brand .brand-square {
    width: 96px;
    height: 96px;
    background: var(--card-white);
  }
  .back-brand .brand-name { color: var(--card-white); }
</style>
</head>
<body>

  <section class="card card--front" aria-label="Business card front">
    <svg class="card-art" viewBox="0 0 620 354" preserveAspectRatio="none">
      <rect width="620" height="354" fill="var(--card-white)"/>
      <rect width="620" height="180" fill="url(#front-sheen)"/>
      <defs>
        <linearGradient id="front-sheen" x1="0" y1="0" x2="0" y2="1">
          <stop offset="0" stop-color="#ffffff"/>
          <stop offset="1" stop-color="#efefef"/>
        </linearGradient>
        <linearGradient id="front-band" x1="0" y1="0" x2="1" y2="1">
          <stop offset="0" stop-color="#a51d23"/>
          <stop offset="1" stop-color="#7c1217"/>
        </linearGradient>
      </defs>
      <path d="M0,170 C180,158 360,108 620,92" fill="none" stroke="var(--cafe-red)" stroke-width="2.5"/>
      <path d="M0,188 C190,176 380,130 620,114 L620,354 L0,354 Z" fill="url(#front-band)"/>
    </svg>

    <div class="brand">
      <div class="brand-square"></div>
      <div class="brand-name">
        <span class="wordmark">Amber Lantern</span>
        <span class="sub">Cafe</span>
      </div>
    </div>

    <div class="contact">
      <p class="person">Daniel Marlow</p>
      <p class="role">managing director</p>
      <dl>
        <dt>phone</dt><dd>555-238-4176</dd>
        <dt>mobile</dt><dd>555-917-3302</dd>
        <dt>email</dt><dd>dmarlow@amberlanterncafe.com</dd>
      </dl>
    </div>

    <div class="location">
      <p>487 Morrow Ave</p>
      <p>Unit 9</p>
      <p>www.amberlanterncafe.com</p>
    </div>
  </section>

  <section class="card card--back" aria-label="Business card back">
    <div class="back-brand">
      <div class="brand-square"></div>
      <div class="brand-name">
        <span class="wordmark">Amber Lantern</span>
        <span class="sub">Cafe</span>
      </div>
    </div>
  </section>

</body>
</html>
```